Brightwell Galley Hour Podcast

We need a Podcast Cover design that is compatible with Apple Podcasts, Spotify, etc. In this podcast, we interview the real movers & shakers in the foodservice industry who cut through the noise to get to the top.

```html
<!DOCTYPE html>
<html lang="en">
<head>
<meta charset="utf-8">
<title>Brightwell Galley Hour Podcast Cover</title>
<link rel="stylesheet" href="https://fonts.googleapis.com/css2?family=Fira+Sans:wght@300&family=Italiana&display=swap">
<style>
  :root {
    --ink: #ffffff;
    --night: #0b0d10;
    --navy: #14243d;
    --amber: #c9a552;
    --gold: #e6cf86;
    --teal: #4f7f86;
    --brown: #3a2a18;
  }
  html, body {
    margin: 0;
    padding: 0;
    width: 1200px;
    height: 1200px;
    overflow: hidden;
    background: var(--night);
  }
  .cover {
    position: relative;
    width: 1200px;
    height: 1200px;
    overflow: hidden;
    background: var(--night);
  }
  .host-photo {
    position: absolute;
    inset: 0;
    background:
      radial-gradient(ellipse 300px 420px at 660px 560px, rgba(20,36,61,0.95), rgba(20,36,61,0) 100%),
      radial-gradient(ellipse 140px 180px at 660px 200px, rgba(176,128,96,0.85), rgba(176,128,96,0) 100%),
      radial-gradient(ellipse 380px 300px at 260px 300px, rgba(230,207,134,0.55), rgba(230,207,134,0) 100%),
      radial-gradient(ellipse 260px 340px at 1060px 380px, rgba(201,165,82,0.6), rgba(201,165,82,0) 100%),
      linear-gradient(90deg, #6c6a3c 0%, #8aa08e 20%, #4f7f86 38%, #3a2a18 60%, #5b3e1c 82%, #8b6a2e 100%);
  }
  .bottom-shade {
    position: absolute;
    inset: 0;
    background: linear-gradient(180deg, rgba(11,13,16,0) 45%, rgba(11,13,16,0.55) 68%, rgba(11,13,16,0.95) 88%, var(--night) 100%);
  }
  .frame {
    position: absolute;
    inset: 17px;
    border: 1.5px solid rgba(255,255,255,0.85);
    pointer-events: none;
  }
  .show-title {
    position: absolute;
    left: 380px;
    top: 755px;
    width: 640px;
    margin: 0;
    color: var(--ink);
    font-family: "Fira Sans", sans-serif;
    font-weight: 300;
    font-size: 74px;
    line-height: 80px;
    text-align: center;
  }
  .host-line {
    position: absolute;
    left: 0;
    top: 0;
    width: 1200px;
    height: 1200px;
  }
  .host-with {
    fill: var(--ink);
    font-family: "Fira Sans", sans-serif;
    font-weight: 300;
    font-size: 24px;
    letter-spacing: 3px;
  }
  .host-name {
    fill: var(--ink);
    font-family: "Italiana", serif;
    font-size: 210px;
  }
</style>
</head>
<body>
  <main class="cover">
    <div class="host-photo" role="img" aria-label="Photo of the smiling host in a navy blazer and light blue shirt, seated in a warmly lit restaurant dining room"></div>
    <div class="bottom-shade"></div>
    <div class="frame"></div>
    <h1 class="show-title">Brightwell<br>Galley Hour</h1>
    <svg class="host-line" viewBox="0 0 1200 1200" aria-label="with Reid Delgado">
      <text class="host-with" x="232" y="985">with</text>
      <text class="host-name" x="50" y="1140" textLength="1090" lengthAdjust="spacingAndGlyphs">ReidDelgado</text>
    </svg>
  </main>
</body>
</html>
```